Corvanta Stationery Design

We need design for our stationary, including:
1) Letterhead
- A4/Letter size in landscape and portrait letterhead
- The letterhead must be in a word file, and the address should be editable using the Felixti or Perpetua Titling TTF
- The output file should be in .docx and in .ai.
2) Business card
- The business card will be printed in white paper and single face only, so there should be nothing on the reverse side.
3) Envelope (sizes A4, Letter, and small document)
Please refer to the picture showing some samples of stationary with designs that would fulfill our wish.
We're including the logo in .AI.
Thanks
Target Market(s)
High end investors
Industry/Entity Type
Landscape
Look and feel
Each slider illustrates characteristics of the customer's brand and the style your logo design should communicate.

```html
<!DOCTYPE html>
<html lang="en">
<head>
<meta charset="utf-8">
<title>Corvanta Stationery</title>
<link href="https://fonts.googleapis.com/css2?family=Cinzel:wght@400;500&family=Montserrat:wght@400;600;700&display=swap" rel="stylesheet">
<style>
  :root {
    --bg: #dcdcdc;
    --paper: #ffffff;
    --ink: #3a3a3a;
    --ink-soft: #6a6a6a;
    --brand-blue: #1574b0;
    --brand-grey: #4d4d4f;
  }
  * { box-sizing: border-box; margin: 0; padding: 0; }
  html, body { width: 1200px; height: 842px; overflow: hidden; background: var(--bg); }
  .canvas { position: relative; width: 1200px; height: 842px; }

  /* Business cards */
  .card {
    position: absolute; top: 40px; width: 350px; height: 200px;
    background: var(--paper); box-shadow: 0 4px 14px rgba(0,0,0,.12);
    font-family: "Montserrat", sans-serif; color: var(--ink);
  }
  .card--stacked { left: 180px; }
  .card--inline { left: 670px; }
  .card__logo {
    position: absolute; left: 28px; top: 78px;
    font-family: "Cinzel", serif; font-weight: 500; font-size: 26px;
    letter-spacing: 2px; color: var(--brand-blue); text-transform: uppercase;
  }
  .card__person { position: absolute; left: 204px; top: 26px; }
  .card__name { font-weight: 700; font-size: 10px; letter-spacing: .5px; text-transform: uppercase; }
  .card__title { font-size: 7px; color: var(--ink-soft); margin-top: 3px; }
  .card__contacts { position: absolute; left: 204px; top: 84px; list-style: none; }
  .card__contacts li { display: flex; align-items: center; gap: 7px; font-size: 7px; height: 13px; }
  .card__contacts svg { width: 7px; height: 7px; fill: var(--brand-blue); }
  .card__address { position: absolute; left: 28px; top: 150px; font-size: 7px; line-height: 10px; }
  .card__bar-grey { position: absolute; left: 0; bottom: 0; width: 45%; height: 7px; background: var(--brand-grey); }
  .card__bar-blue { position: absolute; right: 0; bottom: 7px; width: 55%; height: 4px; background: var(--brand-blue); }
  .card--inline .card__person { left: 204px; }

  /* Envelope */
  .envelope {
    position: absolute; left: 100px; top: 300px; width: 1000px; height: 470px;
    background: var(--paper); box-shadow: 0 6px 18px rgba(0,0,0,.12);
  }
  .envelope__logo {
    position: absolute; left: 60px; top: 345px;
    font-family: "Cinzel", serif; font-weight: 500; font-size: 42px;
    letter-spacing: 3px; color: var(--brand-blue); text-transform: uppercase;
  }
  .envelope__info {
    position: absolute; left: 430px; top: 330px;
    font-family: "Cinzel", serif; font-size: 11px; line-height: 17px;
    color: var(--ink); text-transform: uppercase; letter-spacing: .4px;
  }
  .envelope__company { font-size: 13px; }
  .envelope__label { color: var(--brand-blue); }
  .envelope__bar-grey { position: absolute; left: 0; bottom: 0; width: 38%; height: 14px; background: var(--brand-grey); }
  .envelope__bar-blue { position: absolute; right: 0; bottom: 14px; width: 62%; height: 8px; background: var(--brand-blue); }
</style>
</head>
<body>
<main class="canvas">

  <section class="card card--stacked" aria-label="Business card">
    <div class="card__logo">Corvanta</div>
    <div class="card__person">
      <p class="card__name">Daniel Hartwell</p>
      <p class="card__title">Chairman</p>
    </div>
    <ul class="card__contacts">
      <li><svg viewBox="0 0 10 10"><rect x="2" y="0" width="6" height="10" rx="1"/></svg>+877 555 2140</li>
      <li><svg viewBox="0 0 10 10"><rect x="0" y="2" width="10" height="6"/></svg>daniel@corvanta.com</li>
      <li><svg viewBox="0 0 10 10"><rect x="0" y="1" width="10" height="8" rx="1"/></svg>+877 555 2140</li>
      <li><svg viewBox="0 0 10 10"><circle cx="5" cy="5" r="5"/></svg>www.corvanta.com</li>
    </ul>
    <p class="card__address">218 Harlow Street 3rd Floor<br>Oakland, CA 94607</p>
    <div class="card__bar-blue"></div>
    <div class="card__bar-grey"></div>
  </section>

  <section class="card card--inline" aria-label="Business card">
    <div class="card__logo">Corvanta</div>
    <div class="card__person">
      <p class="card__name">Daniel Hartwell</p>
      <p class="card__title">Chairman</p>
    </div>
    <ul class="card__contacts">
      <li><svg viewBox="0 0 10 10"><rect x="2" y="0" width="6" height="10" rx="1"/></svg>+877 555 2140</li>
      <li><svg viewBox="0 0 10 10"><rect x="0" y="2" width="10" height="6"/></svg>daniel@corvanta.com</li>
      <li><svg viewBox="0 0 10 10"><rect x="0" y="1" width="10" height="8" rx="1"/></svg>+877 555 2140</li>
      <li><svg viewBox="0 0 10 10"><circle cx="5" cy="5" r="5"/></svg>www.corvanta.com</li>
    </ul>
    <p class="card__address">218 Harlow Street 3rd Floor<br>Oakland, CA 94607</p>
    <div class="card__bar-blue"></div>
    <div class="card__bar-grey"></div>
  </section>

  <section class="envelope" aria-label="Envelope">
    <div class="envelope__logo">Corvanta</div>
    <div class="envelope__info">
      <p class="envelope__company">Corvanta Capital Partners, LLC</p>
      <p>218 Harlow Street 3rd Floor, Oakland, California 94607</p>
      <p><span class="envelope__label">Phone:</span> 877.555.2140 • <span class="envelope__label">Fax:</span> 877.555.2141 • <span class="envelope__label">Email:</span> info@corvanta.com • www.corvanta.com</p>
    </div>
    <div class="envelope__bar-blue"></div>
    <div class="envelope__bar-grey"></div>
  </section>

</main>
</body>
</html>
```